WordPress Website Design Project

Technical & Functional Deliverables
WordPress CMS
Fully responsive design
Integrated WhatsApp chatbot
Custom article filtering system
SEO-friendly site structure & performance optimization
CMS user manual & training session

Industry/Entity Type

Industrial Safety and Compliance

Coding

Coded - Design and coding required

Number of Pages Required

5+ page

Font styles to use
Sans Serif

Colors
0054AA
0677BA
7BADD7
CADEEF
E8F1F8

```html
<!DOCTYPE html>
<html lang="en">
<head>
<meta charset="utf-8">
<title>Ravelin — Contact Us</title>
<link href="https://fonts.googleapis.com/css2?family=Poppins:wght@400;500;600;700&display=swap" rel="stylesheet">
<style>
:root{
  --navy:#1f3052;
  --navy-deep:#1b2a48;
  --blue:#5b8fd2;
  --blue-soft:#7badd7;
  --pale:#eef5fc;
  --line:#cadeef;
  --white:#ffffff;
  --ink:#1c2333;
  --req:#d9342b;
}
*{box-sizing:border-box;margin:0;padding:0}
html,body{width:1200px;height:2560px;overflow:hidden;background:var(--white);font-family:'Poppins',sans-serif;color:var(--ink)}
.page{position:relative;width:1200px;height:2560px}
.abs{position:absolute}

/* header */
.brand{display:flex;align-items:center;gap:12px;color:var(--navy);font-weight:700;font-size:54px;letter-spacing:2px;line-height:1}
.brand-mark{width:62px;height:64px;background:var(--blue)}
.site-header .brand{left:68px;top:26px}
.main-nav{left:503px;top:52px;display:flex;align-items:center;font-size:14px;color:var(--navy)}
.main-nav span{display:inline-block}
.main-nav .sep{width:2px;height:14px;background:var(--navy);margin:0 38px}
.nav-cta{left:1011px;top:37px;width:122px;height:46px;background:var(--navy);color:var(--white);font-size:14px;display:flex;align-items:center;justify-content:center;font-weight:500}

/* hero */
.hero{left:0;top:116px;width:1200px;height:700px;overflow:hidden}
.hero-backdrop{left:0;top:0;width:858px;height:700px;background:linear-gradient(180deg,#2c3f63 0%,#23375a 55%,#1f3052 100%)}
.hero-side{left:858px;top:0;width:342px;height:700px;background:linear-gradient(180deg,#84b0dd 0%,#5e8fcc 60%,#4f7fbf 100%)}
.hero-kicker{left:66px;top:128px;color:var(--blue);font-size:38px;font-weight:600}
.hero-title{left:66px;top:178px;color:var(--white);font-weight:700;font-size:78px;line-height:88px}
.hero-title .accent{color:var(--blue)}
.hero-cta{left:69px;top:481px;width:303px;height:80px;border:2px solid var(--white);display:flex;align-items:center;padding-left:42px;gap:38px;color:var(--white);font-size:26px;font-weight:600}
.cta-square{width:32px;height:34px;background:var(--blue)}
.hero-block{left:995px;top:400px;width:173px;height:197px;background:var(--white)}
.hero-frame{left:613px;top:122px;width:532px;height:455px;border:2px solid var(--white)}
.hero-photo{left:622px;top:130px;width:513px;height:442px;background:linear-gradient(135deg,#d9dee5 0%,#a9b3bf 45%,#3b3f48 100%)}

/* section heading */
.section-mark{left:523px;top:930px;display:flex;align-items:center;gap:10px}
.section-mark i{display:block;width:54px;height:3px;background:var(--blue)}
.section-mark b{display:block;width:28px;height:30px;background:var(--blue)}
.section-title{left:0;top:960px;width:1200px;text-align:center;color:var(--navy);font-weight:700;font-size:58px;line-height:70px}

/* contact card */
.contact-info{left:66px;top:1092px;width:468px;height:1010px;background:linear-gradient(180deg,#2a3d61 0%,#24375a 60%,#1f3052 100%)}
.panel-title{font-weight:600;font-size:35px;line-height:44px}
.panel-rule{width:54px;height:3px;background:var(--blue)}
.contact-info .panel-title{left:89px;top:78px;color:var(--white)}
.contact-info .panel-rule{left:89px;top:125px}
.info-item{left:89px;display:flex;gap:22px;color:var(--white)}
.info-icon{width:64px;height:75px;background:var(--blue);display:flex;align-items:center;justify-content:center;flex:none}
.info-head{font-size:21px;font-weight:500;line-height:26px;margin-top:-4px}
.info-text{font-size:14px;line-height:17px;margin-top:2px}
.info-big{font-size:22px;line-height:30px}

.message-form{left:534px;top:1092px;width:604px;height:1010px;background:var(--pale)}
.message-form .panel-title{left:60px;top:78px;color:var(--navy)}
.message-form .panel-rule{left:60px;top:127px}
.field-label{font-size:14px;font-weight:500;color:var(--ink)}
.field-label em{font-style:normal;color:var(--req);margin-right:4px}
.field{background:var(--white);border:1px solid #e3ebf3;box-shadow:0 1px 3px rgba(31,48,82,.08)}
.select{display:flex;align-items:center;justify-content:space-between;padding:0 20px;color:#8a93a3;font-size:14px}
.form-submit{left:62px;top:838px;width:219px;height:76px;background:var(--navy);color:var(--white);display:flex;align-items:center;padding-left:36px;gap:38px;font-size:24px;font-weight:600}

/* footer */
.site-footer{left:0;top:2245px;width:1200px;height:315px;background:var(--navy)}
.footer-about{left:218px;top:70px;color:var(--white);font-size:17px;line-height:27px}
.footer-links{left:804px;top:62px;list-style:none;color:var(--white);font-size:14px;line-height:26px}
.footer-links li{display:flex;align-items:center;gap:10px}
.footer-links li::before{content:"";width:9px;height:9px;background:var(--blue)}
.footer-rule{left:70px;top:202px;width:1063px;height:1px;background:#5a6a88}
.footer-legal{left:70px;top:240px;color:var(--white);font-size:14px}
.social-dot{left:67px;top:2275px;width:26px;height:26px;border-radius:50%;background:var(--blue)}
.copyright{left:482px;top:258px;color:var(--white);font-size:14px}
.site-footer .brand{left:842px;top:230px;color:var(--white)}
</style>
</head>
<body>
<div class="page">

  <header class="site-header">
    <div class="brand abs"><span class="brand-mark"></span>RAVELIN</div>
    <nav class="main-nav abs">
      <span>HOME</span><i class="sep"></i>
      <span>ABOUT US</span><i class="sep"></i>
      <span>SOLUTIONS</span><i class="sep"></i>
      <span>ARTICLES</span>
    </nav>
    <div class="nav-cta abs">CONTACT US</div>
  </header>

  <section class="hero abs">
    <div class="hero-backdrop abs" role="img" aria-label="City office towers under a dark blue overlay"></div>
    <div class="hero-side abs" role="img" aria-label="Glass building facade in light blue tint"></div>
    <div class="hero-kicker abs">Your Partner In</div>
    <h1 class="hero-title abs">INDUSTRIAL<br>SAFETY &amp;<br><span class="accent">Compliance</span></h1>
    <div class="hero-cta abs">CONTACT US <span class="cta-square"></span></div>
    <div class="hero-block abs"></div>
    <div class="hero-frame abs"></div>
    <div class="hero-photo abs" role="img" aria-label="Three colleagues in business attire meeting at a desk with a laptop"></div>
  </section>

  <div class="section-mark abs"><i></i><b></b><i></i></div>
  <h2 class="section-title abs">CONTACT US</h2>

  <section class="contact-info abs">
    <div class="abs" style="inset:0" role="img" aria-label="Support agent wearing a headset, under a navy overlay"></div>
    <h3 class="panel-title abs">Contact Us</h3>
    <div class="panel-rule abs"></div>

    <div class="info-item abs" style="top:243px">
      <div class="info-icon"><svg width="30" height="40" viewBox="0 0 30 40"><path d="M15 1C7 1 1 7 1 15c0 10 14 24 14 24s14-14 14-24C29 7 23 1 15 1z" fill="#fff"/><circle cx="15" cy="15" r="5" fill="#5b8fd2"/></svg></div>
      <div>
        <div class="info-head">LOCATION</div>
        <div class="info-text">Harbourview Point<br>27 Kestrel Quay Road #03-11<br>Singapore 418822</div>
      </div>
    </div>

    <div class="info-item abs" style="top:416px">
      <div class="info-icon"><svg width="36" height="36" viewBox="0 0 24 24"><path d="M6.6 10.8a15 15 0 0 0 6.6 6.6l2.2-2.2c.3-.3.7-.4 1-.2 1.1.4 2.3.6 3.6.6.6 0 1 .4 1 1V20c0 .6-.4 1-1 1A17 17 0 0 1 3 4c0-.6.4-1 1-1h3.5c.6 0 1 .4 1 1 0 1.3.2 2.5.6 3.6.1.3 0 .7-.2 1z" fill="#fff"/></svg></div>
      <div>
        <div class="info-head" style="margin-top:12px">CALL US</div>
        <div class="info-big">+65 6410 2290</div>
      </div>
    </div>

    <div class="info-item abs" style="top:588px">
      <div class="info-icon"><svg width="38" height="28" viewBox="0 0 38 28"><rect x="1" y="1" width="36" height="26" fill="none" stroke="#fff" stroke-width="2"/><path d="M1 1l18 15L37 1M1 27l13-13M37 27L24 14" fill="none" stroke="#fff" stroke-width="2"/></svg></div>
      <div>
        <div class="info-head" style="margin-top:16px">EMAIL US</div>
        <div class="info-text" style="font-size:15px">sales@ravelinsafety.com</div>
      </div>
    </div>
  </section>

  <section class="message-form abs">
    <h3 class="panel-title abs">Send Us A Message</h3>
    <div class="panel-rule abs"></div>

    <div class="field-label abs" style="left:60px;top:180px"><em>*</em>First Name</div>
    <div class="field abs" style="left:60px;top:210px;width:229px;height:48px"></div>
    <div class="field-label abs" style="left:308px;top:180px"><em>*</em>Last Name</div>
    <div class="field abs" style="left:308px;top:210px;width:231px;height:48px"></div>

    <div class="field-label abs" style="left:60px;top:282px"><em>*</em>Country</div>
    <div class="field select abs" style="left:60px;top:312px;width:229px;height:48px">Singapore
      <svg width="14" height="9" viewBox="0 0 14 9"><path d="M1 1l6 6 6-6" fill="none" stroke="#1c2333" stroke-width="2"/></svg></div>
    <div class="field-label abs" style="left:308px;top:282px">Phone</div>
    <div class="field abs" style="left:308px;top:312px;width:231px;height:48px"></div>

    <div class="field-label abs" style="left:60px;top:382px"><em>*</em>E-Mail Address</div>
    <div class="field abs" style="left:60px;top:412px;width:479px;height:48px"></div>

    <div class="field-label abs" style="left:60px;top:482px">Company name</div>
    <div class="field abs" style="left:60px;top:512px;width:479px;height:48px"></div>

    <div class="field-label abs" style="left:60px;top:582px">Job Title</div>
    <div class="field abs" style="left:60px;top:612px;width:479px;height:48px"></div>

    <div class="field-label abs" style="left:60px;top:680px"><em>*</em>Message</div>
    <div class="field abs" style="left:60px;top:708px;width:479px;height:102px"></div>

    <div class="form-submit abs">JOIN US <span class="cta-square"></span></div>
  </section>

  <footer class="site-footer abs">
    <p class="footer-about abs">&nbsp;We are Ravelin. Your<br>Partner in Industrial<br>Safety and Compliance</p>
    <ul class="footer-links abs">
      <li>About Us</li><li>Solutions</li><li>Articles</li><li>Contact Us</li>
    </ul>
    <div class="footer-rule abs"></div>
    <div class="footer-legal abs">Legal | Cookies | Privacy</div>
    <div class="copyright abs">(C) Ravelin (S) Pte Ltd 2025</div>
    <div class="brand abs"><span class="brand-mark"></span>RAVELIN</div>
  </footer>
  <div class="social-dot abs" style="top:2520px"></div>

</div>
</body>
</html>
```